Online-Marketing Material für Nachhilfeschule
Quintessa hat superschnell gearbeitet, vorher selbst recherchiert, um sofort das zu meiner Webseite passende Produkt zu erstellen. Da es eine Kooperation in diesem Fall gab, hat er beide Webseiten für seine Produktvorschläge als Wunschvorstellung ausgesucht und angewendet. Perfekt! That's quintessa! Thank you!
Zielgruppe
Ich habe am 1.7. eine Nachhilfeschule gegründet. Nun möchte ich ein Pilotprojekt starten, um Schülern in der Abiturklasse - Gymnasium oder Berufsschule - , die exzellente Zensuren wollen, zu herausragenden Noten zu verhelfen.
Dieser Banner wird durch den Lehrer den Schülern per Email oder WhatsApp überreicht.
Ich stelle mir ein junges und dynamisches Design vor. Das schwarz/grüne Logo der Fahrschule gefällt mir besser (wenn das andere Eurer Meinung nach besser passt, geht auch das). Das Schwarz-weiß-Logo vom Wissensnest muss aber dominanter sein!
Mein Kooperationspartner, eine Fahrschule, stellt ihre Räume zur Verfügung. Meine Gegenleistung: Nennung in der Werbung.
Aufgabenstellung
Zielgruppe: Abiturienten,
- die Gas geben wollen, damit sie bessere Chancen am Arbeitsmarkt haben.
- die bereit sind, 4 Samstage herzugeben, um noch mehr zu lernen ...
- die selbst, oder deren Eltern, bereit sind, für diese Chancen Geld auszugeben
- die bei der Anmeldung aufgezeigt bekommen, dass das Bonbon eine Vermittlung zu ihrem Wunschunternehmen und ihrer Wunschposition ist.
Das Bonbon bitte Fahrschul-Logo-grün machen, vielleicht auch mit Punkten - vom Wissensnest-Logo ...
Die Texte sind in der Word-Datei. Wichtig: Sie müssen bearbeitet werden können, da sich die Daten wie z.B. Datum, Preis, Fächer, etc. ändern können. Wenn die Kurse angenommen werden, wird der Gewinner zukünftig meine gesamte Werbung gestalten -> CI

```html
<!DOCTYPE html>
<html lang="de">
<head>
<meta charset="utf-8">
<title>Wissensnest – Ich geb Gas fürs Abi</title>
<link rel="stylesheet" href="https://fonts.googleapis.com/css2?family=Raleway:ital,wght@0,400;0,500;0,600;0,700;0,800;1,500;1,900&family=Poppins:wght@600;700&display=swap">
<style>
  :root{
    --blue:#1c4a9c;
    --magenta:#c4157f;
    --ink:#111111;
    --white:#ffffff;
    --cream:#f7f2ef;
    --green:#36e000;
    --grey:#444444;
  }
  *{margin:0;padding:0;box-sizing:border-box}
  html,body{width:848px;height:1200px;overflow:hidden;background:var(--white)}
  .poster{position:relative;width:848px;height:1200px;overflow:hidden;background:var(--white);font-family:"Raleway",sans-serif;color:var(--ink)}
  .backdrop{position:absolute;left:0;top:0;width:848px;height:1200px}
  .abs{position:absolute}

  .brand{left:0;top:72px;width:848px;display:flex;justify-content:center;align-items:center;gap:18px}
  .brand-dot{width:70px;height:70px;border-radius:50%;background:var(--ink)}
  .brand-name{font-family:"Raleway",sans-serif;font-weight:500;font-size:64px;color:var(--ink);letter-spacing:1px}

  .headline{left:0;top:214px;width:848px;text-align:center;font-weight:900;font-style:italic;font-size:58px;color:var(--blue);letter-spacing:-0.5px;white-space:nowrap}
  .headline .accent{color:var(--magenta)}

  .teaser{left:78px;top:302px;width:692px;height:54px;background:var(--magenta);color:var(--white);font-weight:600;font-size:30px;line-height:54px;padding-left:15px;box-shadow:0 4px 8px rgba(0,0,0,.25);z-index:2;white-space:nowrap}
  .teaser-band{left:34px;top:346px;width:780px;height:63px;background:var(--blue);color:var(--white);font-weight:800;font-size:31px;line-height:66px;text-align:center;white-space:nowrap}

  .pole{left:0;top:430px;width:848px;text-align:center;font-weight:800;font-size:25px}

  .bonus-title{left:234px;top:480px;font-weight:700;font-size:32px;color:var(--magenta)}
  .bonus-left{left:182px;top:524px;font-weight:500;font-size:23px}
  .bonus-right{left:475px;top:526px;font-weight:500;font-size:23px}
  .candy{left:378px;top:500px;width:86px;height:66px;border-radius:50%;background:radial-gradient(circle at 35% 35%,#c8ff7a,#4fd300 60%,#2f9e00);transform:rotate(-30deg)}

  .label{background:var(--blue);color:var(--white);font-weight:600;font-size:26px;padding:6px 16px 8px;transform:rotate(-2deg);white-space:nowrap}
  .value{font-family:"Poppins",sans-serif;font-weight:700;font-size:19px;color:var(--white);line-height:1.28}

  .info-intro{left:67px;top:1018px;font-weight:600;font-size:21px;color:var(--blue)}
  .info-phone{left:67px;top:1048px;font-family:"Poppins",sans-serif;font-weight:700;font-size:33px;color:var(--blue)}

  .partner-title{right:58px;top:996px;font-style:italic;font-weight:500;font-size:20px;color:var(--grey)}
  .partner-rule{left:542px;top:1033px;width:5px;height:58px;border-left:2px solid var(--ink);border-right:3px solid var(--green)}
  .partner-name{left:565px;top:1030px;font-weight:800;font-size:26px;color:var(--green)}
  .partner-sub{left:558px;top:1064px;font-style:italic;font-weight:500;font-size:17px;color:var(--grey)}

  .footer{left:0;top:1143px;width:848px;height:57px;background:var(--blue);color:var(--white);font-family:"Poppins",sans-serif;font-weight:700;font-size:18px;text-align:center;line-height:60px}
</style>
</head>
<body>
<main class="poster">
  <svg class="backdrop" viewBox="0 0 848 1200" aria-hidden="true">
    <rect x="0" y="900" width="848" height="300" fill="var(--cream)"/>
    <path fill="var(--magenta)" d="M0,622 C80,612 150,603 210,601 C215,608 190,622 195,628 C240,632 330,612 475,606 C470,612 465,620 490,624 C600,632 700,600 848,590 L848,958 C760,950 640,958 560,965 C480,972 400,975 360,972 C350,965 375,958 370,950 C330,935 200,958 120,968 C60,975 30,972 35,962 C42,955 40,948 0,944 Z"/>
  </svg>

  <header class="abs brand">
    <span class="brand-dot"></span>
    <span class="brand-name">Wissensnest</span>
  </header>

  <h1 class="abs headline">„ICH <span class="accent">GEB GAS</span> FÜRS ABI!“</h1>

  <p class="abs teaser">Du stehst kurz vorm Abi und hast in dir das</p>
  <p class="abs teaser-band">ICH WILL BERUFLICH ERFOLGREICH SEIN-GEN?</p>

  <p class="abs pole">Dann gib Gas und du bist in der Pole-Position!</p>

  <p class="abs bonus-title">Zugabe:</p>
  <p class="abs bonus-left">Unbezahlbares</p>
  <div class="abs candy" role="img" aria-label="Grünes Bonbon"></div>
  <p class="abs bonus-right">für Durchstarter!</p>

  <section class="facts">
    <span class="abs label" style="left:64px;top:650px">wann?</span>
    <p class="abs value" style="left:78px;top:704px">21 Januar 2023</p>

    <span class="abs label" style="left:268px;top:650px">Womit?</span>
    <p class="abs value" style="left:283px;top:704px">Mathe oder Englisch</p>

    <span class="abs label" style="left:543px;top:650px">Wie oft?</span>
    <p class="abs value" style="left:560px;top:704px">An 4 Samstagen,<br>je 2 x 90 Minuten</p>

    <span class="abs label" style="left:61px;top:790px">Wie viele?</span>
    <p class="abs value" style="left:78px;top:846px">2 bis 1 Schüler</p>

    <span class="abs label" style="left:280px;top:790px">Welcher Preis?</span>
    <p class="abs value" style="left:294px;top:846px">290 Euro, inklusive<br>Lernmaterialien</p>

    <span class="abs label" style="left:543px;top:790px">Location?</span>
    <p class="abs value" style="left:560px;top:846px">&nbsp;Tempo Fahrschule,<br>Lindenallee 7,<br>Musterstadt</p>
  </section>

  <p class="abs info-intro">Mehr Infos zur Anmeldung unter</p>
  <p class="abs info-phone">+49 170 555 12 345</p>

  <p class="abs partner-title">Ihre Partner:</p>
  <span class="abs partner-rule"></span>
  <p class="abs partner-name">Tempo Fahrschule</p>
  <p class="abs partner-sub">Ausbildung &amp; Weiterbildung</p>

  <footer class="abs footer">www.wissensnest.de</footer>
</main>
</body>
</html>
```